DeskPilot.dk Frontpage design

I'm in the process of starting a It-course website, based in Denmark. The web site Url is - www.deskpilot.dk

The services are:
- Online courses (This is the main service and the most important)
- One to One courses
- Webinar

I need a frontpage design a simple design, but it must shows professionalism. I have no preference in color, but I like white space.

In Denmark the established competitors are:
- www.trivano.dk (Biggest competitor)
- www.brandlime.dk/online-kurser
- www.selvanu.dk

Target Market(s)

Mainly companies (B to B), but there are also a small number of private customers

Industry/Entity Type

Online it courses and one to one consulting

Number of Pages Required

1 page

Font styles to use
Sans Serif

Requirements
Must have
• A professional design, white space

```html
<!DOCTYPE html>
<html lang="da">
<head>
<meta charset="utf-8">
<title>DeskPilot.dk – Forside</title>
<link href="https://fonts.googleapis.com/css2?family=Lato:wght@400;700;900&display=swap" rel="stylesheet">
<style>
:root{
  --green:#1ec15a;
  --green-dark:#14a54a;
  --green-light:#7ee2a0;
  --ink:#111a14;
  --muted:#7a857e;
  --card:#ffffff;
  --soft:#eef8f1;
  --line:#e3ebe5;
}
*{box-sizing:border-box;margin:0;padding:0}
html,body{width:1200px;height:4064px;overflow:hidden}
body{font-family:'Lato',sans-serif;color:var(--ink);background:#fff;position:relative}
.abs{position:absolute}
.bg{position:absolute;left:0;top:0;width:1200px;height:4064px;z-index:0}
section,header,footer{position:absolute;left:0;width:1200px;z-index:1}

/* header */
.site-header{top:0;height:100px}
.brand{position:absolute;left:112px;top:30px;font-weight:900;font-size:34px;color:var(--green);letter-spacing:-.5px}
.main-nav{position:absolute;left:410px;top:44px;display:flex;gap:24px;font-size:15px;font-weight:700}
.main-nav a{color:#fff;text-decoration:none}
.main-nav a.active{color:var(--ink);border-bottom:2px solid var(--ink)}
.main-nav a.dark{color:var(--ink)}
.login{position:absolute;left:990px;top:34px;background:#fff;color:var(--green);border-radius:22px;padding:10px 22px;font-weight:700;font-size:15px;box-shadow:0 4px 14px rgba(0,0,0,.1)}

/* hero */
.hero{top:100px;height:640px}
.hero h1{position:absolute;left:112px;top:118px;width:520px;font-size:64px;line-height:1.08;font-weight:900}
.hero h1 em{font-style:normal;color:var(--green)}
.btn{display:inline-block;background:var(--green);color:#fff;border-radius:26px;padding:14px 30px;font-weight:700;font-size:16px;box-shadow:0 6px 16px rgba(30,193,90,.35)}
.hero .cta{position:absolute;left:112px;top:392px}
.hero .video{position:absolute;left:288px;top:406px;font-weight:700;color:var(--green);font-size:16px}
.monitor{position:absolute;left:610px;top:60px;width:440px}
.monitor .screen{width:440px;height:300px;background:#222;border-radius:10px;padding:10px}
.monitor .screen div{width:100%;height:100%;border-radius:4px;background:linear-gradient(135deg,#d8dde0,#9aa6a8 60%,#6d7a7c)}
.monitor .chin{width:440px;height:34px;background:#e9ecee;border-radius:0 0 10px 10px}
.monitor .stand{width:110px;height:60px;margin:0 auto;background:linear-gradient(#d4d8da,#b9bec1);clip-path:polygon(25% 0,75% 0,100% 100%,0 100%)}
.scroll{position:absolute;left:586px;top:540px;width:28px;height:42px;border:2px solid var(--green);border-radius:14px}
.scroll:after{content:"";position:absolute;left:11px;top:8px;width:3px;height:9px;background:var(--green);border-radius:2px}

h2.title{position:absolute;left:0;width:1200px;text-align:center;font-size:56px;font-weight:900}
h2.title span{color:var(--green)}
.sub{position:absolute;left:0;width:1200px;text-align:center;font-size:16px;color:var(--muted)}

/* courses */
.courses{top:740px;height:580px}
.course{position:absolute;width:300px;text-align:center;padding:40px 24px;border-radius:22px;background:#fff}
.course.raised{box-shadow:0 20px 50px rgba(0,0,0,.12);top:190px}
.course .icon{width:64px;height:64px;margin:0 auto 26px;border-radius:16px;background:var(--soft);border:3px solid var(--green)}
.course h3{font-size:22px;font-weight:900;line-height:1.25;margin-bottom:14px}
.course p{font-size:14px;color:var(--muted);line-height:1.5;margin-bottom:20px}
.tag{display:inline-block;background:var(--green);color:#fff;font-size:12px;font-weight:900;padding:7px 16px;border-radius:14px;margin:0 4px}

/* why */
.why{top:1320px;height:720px}
.why-card{position:absolute;width:230px;height:300px;background:#fff;border-radius:18px;box-shadow:0 16px 40px rgba(0,0,0,.12);text-align:center;padding:34px 20px}
.why-card .hex{width:90px;height:90px;margin:0 auto 22px;background:var(--green);clip-path:polygon(50% 0,93% 25%,93% 75%,50% 100%,7% 75%,7% 25%);display:flex;align-items:center;justify-content:center}
.why-card h3{font-size:22px;font-weight:900;margin-bottom:12px}
.why-card p{font-size:13px;color:var(--muted);line-height:1.5}

/* webinar */
.webinar{top:2040px;height:420px}
.webinar .photo{position:absolute;left:150px;top:20px;width:430px;height:330px;border-radius:14px;background:linear-gradient(135deg,#f0e6d8,#c8b39a 55%,#8a7560)}
.webinar .play{position:absolute;left:330px;top:150px;width:62px;height:62px;border-radius:50%;background:var(--green);box-shadow:0 0 0 12px rgba(30,193,90,.3)}
.webinar .play:after{content:"";position:absolute;left:24px;top:19px;border-left:18px solid #fff;border-top:12px solid transparent;border-bottom:12px solid transparent}
.webinar h2{position:absolute;left:618px;top:20px;font-size:56px;font-weight:900}
.webinar ul{position:absolute;left:618px;top:112px;width:460px;list-style:none}
.webinar li{font-size:14px;color:var(--muted);line-height:1.55;margin-bottom:14px;padding-left:22px;position:relative}
.webinar li:before{content:"";position:absolute;left:0;top:6px;width:9px;height:9px;border-radius:50%;background:var(--green)}
.webinar .btn{position:absolute;left:618px;top:290px}

/* services */
.services{top:2460px;height:560px}
.service{position:absolute;width:300px;height:330px;background:#fff;border-radius:22px;box-shadow:0 14px 40px rgba(0,0,0,.1);text-align:center}
.service .art{width:220px;height:190px;margin:34px auto 20px;border-radius:50%;background:radial-gradient(circle at 50% 60%,#c7efd5,#eaf8ef 70%)}
.service h3{font-size:26px;font-weight:900}

/* blog */
.blog{top:3100px;height:520px}
.blog h2{position:absolute;left:0;width:1200px;text-align:center;top:130px;font-size:56px;font-weight:900;color:#fff}
.post{position:absolute;top:236px;width:420px;height:180px;background:#fff;border-radius:40px 0 40px 0;text-align:center;padding:30px 20px}
.post h3{font-size:22px;font-weight:900;margin-bottom:14px}
.post p{font-size:14px;color:var(--muted);margin-bottom:16px}
.post a{font-size:15px;font-weight:900;color:var(--green);text-decoration:none}
.arrow{position:absolute;top:300px;width:52px;height:52px;border:3px solid #fff;border-radius:50%}

/* footer */
.site-footer{top:3620px;height:444px}
.site-footer .brand{left:112px;top:90px}
.social{position:absolute;left:112px;top:150px;display:flex;gap:8px}
.social span{width:30px;height:30px;border-radius:50%;border:2px solid var(--ink)}
.fcol{position:absolute;top:90px}
.fcol h4{font-size:30px;font-weight:900;margin-bottom:20px}
.fcol a{display:block;font-size:15px;color:var(--muted);text-decoration:none;margin-bottom:10px}
.newsletter{position:absolute;left:808px;top:156px;width:280px;height:48px;border:1px solid var(--line);border-radius:24px;font-size:13px;color:var(--muted);padding:15px 20px}
.newsletter b{position:absolute;right:0;top:0;height:46px;background:var(--green);color:#fff;border-radius:24px;padding:15px 22px;font-size:13px}
.copy{position:absolute;left:0;top:376px;width:1200px;text-align:center;font-size:13px;color:var(--muted)}
.copy-rule{position:absolute;left:112px;top:350px;width:976px;height:1px;background:var(--line)}
</style>
</head>
<body>

<svg class="bg" viewBox="0 0 1200 4064" aria-hidden="true">
  <!-- hero shapes -->
  <polygon points="480,0 1200,0 1200,640 1000,740" fill="var(--green)"/>
  <polygon points="1060,300 1200,200 1200,760" fill="var(--green-light)" opacity=".7"/>
  <polygon points="0,560 140,740 0,740" fill="var(--soft)"/>
  <!-- why band -->
  <polygon points="0,1330 420,1560 0,1980" fill="var(--green)"/>
  <polygon points="1200,1320 760,1620 1200,1960" fill="var(--green)"/>
  <polygon points="0,1450 0,1700 220,1560" fill="var(--green-light)" opacity=".6"/>
  <polygon points="1200,1500 1000,1640 1200,1800" fill="var(--green-light)" opacity=".6"/>
  <!-- dots -->
  <g fill="var(--green)" opacity=".5">
    <circle cx="470" cy="1260" r="3"/><circle cx="486" cy="1260" r="3"/><circle cx="502" cy="1260" r="3"/><circle cx="518" cy="1260" r="3"/>
    <circle cx="470" cy="1276" r="3"/><circle cx="486" cy="1276" r="3"/><circle cx="502" cy="1276" r="3"/><circle cx="518" cy="1276" r="3"/>
    <circle cx="470" cy="1292" r="3"/><circle cx="486" cy="1292" r="3"/><circle cx="502" cy="1292" r="3"/><circle cx="518" cy="1292" r="3"/>
    <circle cx="760" cy="2660" r="3"/><circle cx="776" cy="2660" r="3"/><circle cx="792" cy="2660" r="3"/><circle cx="760" cy="2676" r="3"/><circle cx="776" cy="2676" r="3"/><circle cx="792" cy="2676" r="3"/>
  </g>
  <!-- blog band -->
  <polygon points="0,3110 1200,3110 1200,3620 0,3560" fill="var(--green)"/>
  <polygon points="0,3110 500,3110 0,3380" fill="var(--green-dark)" opacity=".35"/>
</svg>

<header class="site-header">
  <div class="brand">deskpilot</div>
  <nav class="main-nav">
    <a class="active">Hjem</a><a class="dark">Kurser</a><a class="dark">webinar</a><a>En til en</a><a>Spørgsmål</a><a>Blog</a><a>Om</a><a>Kontakt</a>
  </nav>
  <div class="login">Log ind</div>
</header>

<section class="hero">
  <h1>Styrk dine it kundskaber med <em>“just-in-time”</em> learning</h1>
  <span class="btn cta">Kom igang ➜</span>
  <span class="video">▶ Se Video</span>
  <div class="monitor">
    <div class="screen"><div role="img" aria-label="Foto af en mand med briller, der arbejder ved en computer"></div></div>
    <div class="chin"></div>
    <div class="stand"></div>
  </div>
  <div class="scroll"></div>
</section>

<section class="courses">
  <h2 class="title" style="top:20px">Udvalgte <span>kurser</span></h2>
  <p class="sub" style="top:104px">Find dit næste online kursus her</p>
  <div class="course" style="left:128px;top:160px">
    <div class="icon"></div>
    <h3>Dataflow BI<br>på én time</h3>
    <p>Er det muligt at lære Dataflow BI på kun én time? Helt klart, her får du en hurtig introduktion.</p>
    <span class="tag">DATAFLOW</span>
  </div>
  <div class="course raised" style="left:450px">
    <div class="icon"></div>
    <h3>Pyra for Tabula<br>brugere</h3>
    <p>Hvordan kommer du som Tabula-bruger i gang med at bruge Pyra.</p>
    <span class="tag">PYRA</span><span class="tag">TABULA</span>
  </div>
  <div class="course" style="left:772px;top:160px">
    <div class="icon"></div>
    <h3>Rho Introduktion</h3>
    <p>Introduktion til Rho programmering.</p>
    <span class="tag">RHO</span>
  </div>
</section>

<section class="why">
  <h2 class="title" style="top:130px">Hvorfor <span>DeskPilot?</span></h2>
  <p class="sub" style="top:212px">Jeg har siden 1995 undervist rigtig mange glade kursister.</p>
  <div class="why-card" style="left:110px;top:280px">
    <div class="hex"><svg width="36" height="36" viewBox="0 0 24 24" fill="none" stroke="#fff" stroke-width="2"><circle cx="12" cy="12" r="9"/><path d="M12 7v10M9 10h5a2 2 0 010 4H9"/></svg></div>
    <h3>God økonomi</h3><p>Prisen på et online kursus er ¼ af et fysisk kursus.</p>
  </div>
  <div class="why-card" style="left:356px;top:330px">
    <div class="hex"><svg width="36" height="36" viewBox="0 0 24 24" fill="none" stroke="#fff" stroke-width="2"><path d="M9 18h6M10 21h4M12 3a6 6 0 00-3 11v2h6v-2a6 6 0 00-3-11z"/></svg></div>
    <h3>Hvorfor vente</h3><p>Styrk dine kompetencer på et online kursus nu.</p>
  </div>
  <div class="why-card" style="left:602px;top:280px">
    <div class="hex"><svg width="36" height="36" viewBox="0 0 24 24" fill="none" stroke="#fff" stroke-width="2"><circle cx="12" cy="12" r="9"/><path d="M12 7v5l3 2"/></svg></div>
    <h3>Ingen rejsetid</h3><p>Du sparer for spildtid og deltimer, når du er hjemme.</p>
  </div>
  <div class="why-card" style="left:848px;top:330px">
    <div class="hex"><svg width="36" height="36" viewBox="0 0 24 24" fill="none" stroke="#fff" stroke-width="2"><rect x="3" y="5" width="18" height="14" rx="2"/><path d="M3 9h18"/></svg></div>
    <h3>Designet i en Browser</h3><p>Designet i en browser, altid opdateret og nem at bruge.</p>
  </div>
</section>

<section class="webinar">
  <div class="photo" role="img" aria-label="Foto af en person med headset, der deltager i et webinar ved et skrivebord"></div>
  <div class="play"></div>
  <h2>Webinar</h2>
  <ul>
    <li>Det er ikke kun på jorden at webinarer står i stedet for kurser og møder.</li>
    <li>Du får den samme høje kvalitet på et webinar som på et traditionelt kursus, og kan deltage hvor du end befinder dig.</li>
    <li>Det bedste af det hele er, at du kan gense det hele bagefter i dit eget tempo.</li>
  </ul>
  <span class="btn">Lær mere ➜</span>
</section>

<section class="services">
  <h2 class="title" style="top:40px">Vores <span>tjenester</span></h2>
  <div class="service" style="left:112px;top:160px"><div class="art" role="img" aria-label="Illustration af en person, der tager et online kursus på en bærbar"></div><h3>Online kurser</h3></div>
  <div class="service" style="left:450px;top:130px"><div class="art" role="img" aria-label="Illustration af to personer i en én-til-én undervisning"></div><h3>En til en kurser</h3></div>
  <div class="service" style="left:788px;top:160px"><div class="art" role="img" aria-label="Illustration af en underviser, der holder webinar foran en skærm"></div><h3>Webinar</h3></div>
</section>

<section class="blog">
  <h2>Seneste blogindlæg</h2>
  <div class="arrow" style="left:10px"><svg width="46" height="46" viewBox="0 0 46 46"><path d="M28 14l-10 9 10 9" stroke="#fff" stroke-width="3" fill="none"/></svg></div>
  <div class="post" style="left:150px"><h3>Løbende sum</h3><p>Opsætning af løbende totaler</p><a>Read More Article</a></div>
  <div class="post" style="left:630px"><h3>Brug Dataflow BI data i Tabula</h3><p>Opsætning af løbende totaler</p><a>Read More Article</a></div>
  <div class="arrow" style="right:10px"><svg width="46" height="46" viewBox="0 0 46 46"><path d="M18 14l10 9-10 9" stroke="#fff" stroke-width="3" fill="none"/></svg></div>
</section>

<footer class="site-footer">
  <div class="brand">deskpilot</div>
  <div class="social"><span></span><span></span><span></span><span></span></div>
  <div class="fcol" style="left:350px"><h4>hurtige links</h4><a>Kurser</a><a>Webinar</a><a>En til En</a><a>Spørgsmål</a></div>
  <div class="fcol" style="left:584px"><h4>Information</h4><a>Blog</a><a>Om</a><a>Kontakt</a><a>Terms</a></div>
  <div class="fcol" style="left:808px"><h4>Holde kontakt</h4></div>
  <div class="newsletter">Indtast din e-mail<b>ABONNER</b></div>
  <div class="copy-rule"></div>
  <p class="copy">© Copyright 2022 DeskPilot. Alle rettigheder forbeholdes</p>
</footer>

</body>
</html>
```